New Business Card Design Project

I need a clean, professional business card. I'd like it to have some color, but not be wild. We do technology consulting and we have clients large and small who trust us with some of their most important data and projects. Simple but not boring should drive all design proposals. Multicolored and two sided, but with a matte finish, I think.
For more on tone, check out our website: http://quorvantis.example

Target Market(s)

Upper management of respected businesses. Tech savvy, but not "hipster".

Industry/Entity Type

Business

Requirements
Must have
• Files need to be provided in .eps and in .pdf in a manner that allows for easy updates.
Must have Name, Title, Phone, Email, Twitter, Website
Nice to have
• Logo/Name shouldn't be too big. One thing I've read several places is that the bigger the logo, the smaller the brand. A good article on dos and don'ts here: http://www.brindlepost.example/2011/02/business-card-experience.html

```html
<!DOCTYPE html>
<html lang="en">
<head>
<meta charset="utf-8">
<title>Quorvantis Business Card</title>
<link href="https://fonts.googleapis.com/css2?family=Arimo:wght@400;700&display=swap" rel="stylesheet">
<style>
  :root {
    --teal: #3b8f9e;
    --white: #ffffff;
    --ink: #5b5b5b;
    --dark: #2b2b2b;
    --backdrop: #ece9e4;
    --accent: #8dac3e;
  }
  * { box-sizing: border-box; margin: 0; padding: 0; }
  html, body {
    width: 1200px; height: 702px; overflow: hidden;
    background: var(--backdrop);
    font-family: "Arimo", Arial, sans-serif;
  }
  .stage { position: relative; width: 1200px; height: 702px; }
  .card {
    position: absolute; top: 190px;
    width: 540px; height: 320px;
    border-radius: 18px; overflow: hidden;
    box-shadow: 0 6px 18px rgba(0,0,0,.18);
  }
  .card-front { left: 45px; background: var(--white); }
  .card-back { left: 615px; background: var(--teal); }

  .brand {
    position: absolute; left: 70px; top: 68px;
    display: flex; align-items: center; gap: 16px;
  }
  .brand-dot { width: 26px; height: 26px; border-radius: 50%; background: var(--accent); }
  .brand-name {
    font-size: 46px; font-weight: 400; letter-spacing: 2px;
    color: var(--ink); text-transform: uppercase;
  }

  .contact-band {
    position: absolute; left: 0; top: 178px; width: 100%; height: 92px;
    background: var(--teal); color: var(--white);
    display: flex; align-items: center; justify-content: center; gap: 16px;
  }
  .person { text-align: right; }
  .person-name { font-size: 21px; font-weight: 700; }
  .person-title { font-size: 14px; margin-top: 2px; }
  .divider { width: 1px; height: 62px; background: var(--white); }
  .contact-list { list-style: none; font-size: 14px; line-height: 21px; }
  .contact-list li { display: flex; align-items: center; gap: 7px; }
  .contact-list svg { width: 12px; height: 12px; flex: none; }
  .handle-square { width: 11px; height: 11px; background: #6fb8e0; flex: none; }

  .site-front {
    position: absolute; left: 0; bottom: 0; width: 100%; height: 50px;
    display: flex; align-items: center; justify-content: center;
    font-size: 15px; letter-spacing: 3px; color: var(--dark);
  }

  .back-brand {
    position: absolute; left: 0; top: 100px; width: 100%;
    display: flex; align-items: center; justify-content: center; gap: 18px;
  }
  .back-dot { width: 34px; height: 34px; border-radius: 50%; background: var(--white); }
  .back-name {
    font-size: 52px; font-weight: 400; letter-spacing: 3px;
    color: var(--white); text-transform: uppercase;
  }
  .site-back {
    position: absolute; left: 0; bottom: 48px; width: 100%; text-align: center;
    font-size: 16px; font-weight: 700; letter-spacing: 4px; color: var(--white);
  }
</style>
</head>
<body>
<main class="stage">
  <section class="card card-front" aria-label="Card front">
    <div class="brand">
      <span class="brand-dot"></span>
      <span class="brand-name">Quorvantis</span>
    </div>
    <div class="contact-band">
      <div class="person">
        <p class="person-name">Your Name</p>
        <p class="person-title">Title</p>
      </div>
      <span class="divider"></span>
      <ul class="contact-list">
        <li>
          <svg viewBox="0 0 12 12" aria-hidden="true"><path d="M2.5 1 L4.5 1 L5.3 3.6 L4 4.6 C4.6 6 5.8 7.3 7.3 8 L8.4 6.7 L11 7.5 L11 9.5 C11 10.4 10.3 11 9.5 11 C5 10.7 1.3 7 1 2.5 C1 1.7 1.6 1 2.5 1Z" fill="#fff"/></svg>
          <span>0912 345678</span>
        </li>
        <li>
          <svg viewBox="0 0 12 12" aria-hidden="true"><rect x="0.5" y="2" width="11" height="8" fill="none" stroke="#fff" stroke-width="1.3"/><path d="M0.5 2.5 L6 7 L11.5 2.5" fill="none" stroke="#fff" stroke-width="1.3"/></svg>
          <span>info@quorvantis.example</span>
        </li>
        <li>
          <span class="handle-square"></span>
          <span>@quorvantis</span>
        </li>
      </ul>
    </div>
    <p class="site-front">www.quorvantis.example</p>
  </section>

  <section class="card card-back" aria-label="Card back">
    <div class="back-brand">
      <span class="back-dot"></span>
      <span class="back-name">Quorvantis</span>
    </div>
    <p class="site-back">www.quorvantis.example</p>
  </section>
</main>
</body>
</html>
```